Corkbell Cellars: the premier wine registry - (need business cards)

We have a logo designed, and now we need business cards for our 3 founders. Corkbell Cellars is the premier wine registry for weddings. I am envisioning the wine glass with the heart in it as our signature symbol. (FYI- on the red background file, only use the part that has the red background; the brown colors are not relevant)

```html
<!DOCTYPE html>
<html lang="en">
<head>
<meta charset="utf-8">
<title>Corkbell Cellars – Business Cards</title>
<link href="https://fonts.googleapis.com/css2?family=Montserrat:wght@300;400;500&family=Roboto:wght@400;500;700&display=swap" rel="stylesheet">
<style>
  :root {
    --backdrop: #2b2b2b;
    --wine: #98244f;
    --paper: #ffffff;
    --silver: #d3d3d5;
    --ink: #1f1f1f;
  }
  html, body {
    margin: 0;
    width: 1200px;
    height: 900px;
    overflow: hidden;
    background: var(--backdrop);
  }
  .stage {
    position: relative;
    width: 1200px;
    height: 900px;
  }
  .card {
    position: absolute;
    width: 600px;
    height: 343px;
    border-radius: 16px;
    overflow: hidden;
    box-shadow: 0 10px 30px rgba(0,0,0,.45);
  }

  /* Front */
  .card-front {
    left: 70px;
    top: 80px;
    background: var(--wine);
    color: var(--paper);
  }
  .front-brand {
    position: absolute;
    left: 0; right: 0;
    top: 140px;
    text-align: center;
    font-family: "Montserrat", sans-serif;
    font-weight: 300;
    font-size: 32px;
    letter-spacing: 8px;
  }
  .front-brand .mark {
    display: inline-block;
    width: 14px; height: 14px;
    border-radius: 50%;
    background: var(--paper);
    margin-right: 16px;
    vertical-align: middle;
  }
  .front-web {
    position: absolute;
    left: 0; right: 0;
    bottom: 46px;
    text-align: center;
    font-family: "Roboto", sans-serif;
    font-size: 13px;
    letter-spacing: .3px;
  }

  /* Back */
  .card-back {
    left: 530px;
    top: 477px;
    background: var(--paper);
  }
  .back-panel {
    position: absolute;
    inset: 0;
    background: var(--wine);
    clip-path: polygon(44% 0, 100% 0, 100% 100%, 58% 100%);
    filter: drop-shadow(-4px 0 6px rgba(0,0,0,.25));
  }
  .name-ribbon {
    position: absolute;
    top: 34px;
    right: 0;
    width: 380px;
    height: 64px;
    background: var(--silver);
    clip-path: polygon(0 0, 100% 0, 100% 100%, 4% 100%);
    text-align: center;
    font-family: "Roboto", sans-serif;
    color: var(--wine);
    padding-top: 12px;
    box-sizing: border-box;
  }
  .name-ribbon .person {
    font-weight: 700;
    font-size: 19px;
    letter-spacing: .3px;
  }
  .name-ribbon .role {
    font-size: 11px;
    margin-top: 2px;
  }
  .back-brand {
    position: absolute;
    left: 36px;
    top: 108px;
    display: flex;
    align-items: center;
    gap: 12px;
    font-family: "Montserrat", sans-serif;
    font-weight: 400;
    font-size: 22px;
    line-height: 1.2;
    letter-spacing: 4px;
    color: var(--wine);
  }
  .back-brand .mark {
    width: 14px; height: 14px;
    border-radius: 50%;
    background: var(--wine);
    flex: none;
  }
  .back-brand .words span { display: block; }
  .contacts {
    position: absolute;
    left: 36px;
    bottom: 30px;
    margin: 0;
    padding: 0;
    list-style: none;
    font-family: "Roboto", sans-serif;
    font-size: 13.5px;
    color: var(--ink);
  }
  .contacts li {
    display: flex;
    align-items: center;
    gap: 10px;
    height: 25px;
  }
  .contacts .icon {
    width: 20px; height: 20px;
    background: var(--wine);
    display: flex;
    align-items: center;
    justify-content: center;
  }
  .address {
    position: absolute;
    right: 34px;
    bottom: 42px;
    width: 240px;
    text-align: center;
    font-family: "Roboto", sans-serif;
    font-size: 13.5px;
    line-height: 1.35;
    color: var(--paper);
  }
  .address svg { display: block; margin: 0 auto 6px; }
</style>
</head>
<body>
<main class="stage">

  <section class="card card-front">
    <div class="front-brand"><span class="mark"></span>CORKBELL CELLARS</div>
    <div class="front-web">www.corkbellcellars.com</div>
  </section>

  <section class="card card-back">
    <div class="back-panel"></div>

    <div class="name-ribbon">
      <div class="person">MILES HARLOW</div>
      <div class="role">Founder &amp; Director</div>
    </div>

    <div class="back-brand">
      <span class="mark"></span>
      <div class="words"><span>CORKBELL</span><span>CELLARS</span></div>
    </div>

    <ul class="contacts">
      <li><span class="icon"><svg width="12" height="12" viewBox="0 0 24 24"><path fill="#fff" d="M6.6 10.8a15 15 0 0 0 6.6 6.6l2.2-2.2c.3-.3.7-.4 1-.2 1.1.4 2.3.6 3.6.6.6 0 1 .4 1 1V20c0 .6-.4 1-1 1A17 17 0 0 1 3 4c0-.6.4-1 1-1h3.5c.6 0 1 .4 1 1 0 1.3.2 2.5.6 3.6.1.3 0 .7-.2 1z"/></svg></span>555-610-2048</li>
      <li><span class="icon"><svg width="12" height="12" viewBox="0 0 24 24"><rect x="3" y="8" width="18" height="12" rx="2" fill="#fff"/><rect x="6" y="3" width="12" height="6" rx="1" fill="none" stroke="#fff" stroke-width="2"/></svg></span>555-610-2049</li>
      <li><span class="icon"><svg width="12" height="10" viewBox="0 0 24 18"><rect x="1" y="1" width="22" height="16" fill="none" stroke="#fff" stroke-width="2"/><path d="M1 1l11 9 11-9" fill="none" stroke="#fff" stroke-width="2"/></svg></span>hello@corkbellcellars.com</li>
      <li><span class="icon"><svg width="12" height="12" viewBox="0 0 24 24"><circle cx="12" cy="12" r="10" fill="none" stroke="#fff" stroke-width="2"/><path d="M2 12h20M12 2c3 3 3 17 0 20M12 2c-3 3-3 17 0 20" fill="none" stroke="#fff" stroke-width="1.6"/></svg></span>www.corkbellcellars.com</li>
    </ul>

    <div class="address">
      <svg width="12" height="16" viewBox="0 0 24 32"><path fill="#fff" d="M12 0A12 12 0 0 0 0 12c0 9 12 20 12 20s12-11 12-20A12 12 0 0 0 12 0zm0 17a5 5 0 1 1 0-10 5 5 0 0 1 0 10z"/></svg>
      48 Vine Row - Maple Falls<br>Oregon 97321
    </div>
  </section>

</main>
</body>
</html>
```